Business Profile Landing Page for search engine Start UP " Amber Quill"

Hi there
Amber Quill is an search engine for the Amber Quill - business.

What i´m looking for is a stunning singel Profile Landing Page for the Companys presentation.

Following Details should be included.

1st section
Comapanys name
Adress
info row ( opening time or what ever)
Profile Picture Big ( Could be the logo)
+3 smaller Pictures ( Maybe the store, main product ...)

2nd Section
navigation Icons for:
Call, Mail , Web, Route, Data

3er Section
About us.

Text lines.....
+Pictures slider

4th Section
1 row : Products ( Titel , Picture, Price)
2nd row :Service ( same as Products + text lines )

5th section
Blog Posts row

.....................................................
Well thats all, Colors used from the logo, u can also use the favicon somewhere (the crown magnifying glass)

Target Market(s)

All Comapnys, it should be an " used for all" design

Number of Pages Required

1 page

Requirements
Must have
• The first sighting is the important part, so the " first section should be impressively and makes the customers curious about more informations (very important for mobile version)
Nice to have
• If you can insert our favicon somewhere would be cool, but its not nessesery
Should not have
• you dont need to make a header or footer, that part is already done. i just need the main section design

```html
<!DOCTYPE html>
<html lang="en">
<head>
<meta charset="utf-8">
<title>Amber Quill – Business Profile</title>
<link href="https://fonts.googleapis.com/css2?family=Catamaran:wght@400;600;700;800&family=Nunito:wght@400;600;700&display=swap" rel="stylesheet">
<style>
:root{
  --gold:#c8820f;
  --gold-dark:#b57408;
  --ink:#111111;
  --text:#333333;
  --muted:#555555;
  --light-bg:#efefef;
  --line:#dddddd;
  --white:#ffffff;
}
*{box-sizing:border-box;margin:0;padding:0}
html,body{width:1200px;height:3422px;overflow:hidden;background:var(--white)}
body{font-family:"Nunito",Arial,sans-serif;color:var(--text);position:relative}
.wrap{width:978px;margin:0 auto;position:relative}

/* top info bar */
.info-bar{height:62px;background:#000;color:#ddd;font-size:14px}
.info-bar .wrap{display:flex;justify-content:space-between;align-items:center;height:62px}
.info-bar span{display:flex;align-items:center;gap:10px}
.info-bar svg{width:13px;height:13px;fill:#ddd}

/* header */
.site-header{height:131px;background:var(--white)}
.site-header .wrap{display:flex;justify-content:space-between;align-items:center;height:131px}
.brand{font-family:"Catamaran",sans-serif;font-weight:800;font-size:42px;color:var(--gold);line-height:1}
.brand small{display:block;font-family:"Catamaran",sans-serif;font-weight:800;font-size:27px;color:var(--gold);margin-top:4px;letter-spacing:.3px}
.quick-nav{display:flex;gap:48px}
.quick-nav a{display:flex;flex-direction:column;align-items:center;gap:14px;text-decoration:none;color:#333;font-size:17px}
.quick-nav svg{width:18px;height:18px;fill:var(--gold)}

/* hero */
.hero{position:relative;height:692px;background:linear-gradient(120deg,#4a4038 0%,#2f3a4c 40%,#1d2a44 70%,#0f1a33 100%);text-align:center;color:var(--white)}
.hero-title{position:absolute;top:355px;left:0;right:0;font-family:"Catamaran",sans-serif;font-weight:800;font-size:96px;line-height:1;color:var(--white)}
.hero-sub{position:absolute;top:480px;left:0;right:0;font-family:"Catamaran",sans-serif;font-weight:400;font-size:32px}
.thumbs{position:absolute;top:620px;left:302px;display:flex;gap:9px}
.thumb{width:193px;height:133px}
.thumb.active{outline:3px solid var(--gold);outline-offset:-3px}
.t1{background:linear-gradient(135deg,#5b6272,#2b3550)}
.t2{background:linear-gradient(135deg,#3e4654,#1a2d46 60%,#7c3b4a)}
.t3{background:linear-gradient(135deg,#e6e6e8,#9db4d6 70%,#5b7fb8)}

/* section headings */
.heading{font-family:"Catamaran",sans-serif;font-weight:700;font-size:48px;color:var(--ink);line-height:1}
.heading em{font-style:normal;color:var(--gold)}
.heading-center{text-align:center}
.rule{width:50px;height:2px;background:var(--gold);margin:18px auto 0}

/* about */
.about{height:631px;position:relative}
.about .heading{position:absolute;top:178px;left:0}
.about-text{position:absolute;top:253px;left:0;width:435px;font-family:Arial,sans-serif;font-size:13.5px;line-height:27.5px;color:#444;text-align:justify}
.btn{display:inline-block;background:var(--gold);color:var(--white);font-size:16px;font-weight:600;text-decoration:none;border-radius:2px}
.about .btn{position:absolute;top:500px;left:0;width:118px;height:48px;line-height:48px;text-align:center}
.about-slider{position:absolute;top:192px;left:504px;width:474px;height:356px;background:linear-gradient(135deg,#4a4f56,#7a7f86 45%,#c7c9cc 80%,#9a9ea4)}
.dots{position:absolute;bottom:12px;left:212px;display:flex;gap:10px}
.dots i{width:8px;height:8px;border-radius:50%;background:var(--white)}

/* products */
.products{background:var(--light-bg);height:604px;padding-top:60px}
.cards{display:flex;justify-content:space-between;margin-top:30px}
.product{width:309px;height:382px;background:var(--white);border:1px solid var(--line);text-align:center;padding-top:36px}
.product .pic{width:150px;height:140px;margin:0 auto;border-radius:6px}
.p1{background:linear-gradient(135deg,#f3b24a,#d5862a)}
.p2{background:linear-gradient(135deg,#e8e3c8,#d8232a 60%,#8fb06a)}
.p3{background:linear-gradient(135deg,#f04a2a,#c2261b)}
.price{font-family:"Catamaran",sans-serif;font-weight:700;font-size:24px;color:var(--gold);margin-top:34px}
.pname{font-family:"Catamaran",sans-serif;font-weight:600;font-size:24px;color:var(--ink);margin-top:6px}
.pdesc{font-family:Arial,sans-serif;font-size:13px;line-height:26px;color:#555;margin:14px auto 0;width:260px}

/* services */
.services{height:609px;padding-top:72px}
.service-row{display:flex;justify-content:space-between;margin-top:40px}
.service{width:232px;height:362px;border:1px solid var(--line);text-align:center}
.service .pic{height:275px}
.s1{background:linear-gradient(135deg,#d8c9a8,#b8a27e 50%,#e0d3b8)}
.s2{background:linear-gradient(135deg,#c9c6c4,#2c3b4f 60%,#1f2a3a)}
.s3{background:linear-gradient(135deg,#e9ecef,#7d8794 60%,#c94b4b)}
.s4{background:linear-gradient(135deg,#3a3a3a,#d7d7d7 50%,#f4f4f4)}
.service p{font-family:"Nunito",sans-serif;font-size:18px;line-height:24px;color:#333;padding-top:19px}

/* blog */
.blog{display:flex;height:507px}
.blog-pic{width:563px;background:linear-gradient(135deg,#7a5a3a,#a27d52 40%,#e7e0cf 70%,#8a6a44)}
.blog-body{flex:1;background:var(--gold);color:var(--white);padding:62px 140px 0 45px}
.blog-body .heading{color:var(--white);font-weight:600}
.blog-body .rule{background:var(--white);margin:20px 0 0}
.blog-meta{font-size:16px;margin-top:25px}
.blog-text{font-family:Arial,sans-serif;font-size:13.5px;line-height:27.5px;text-align:justify;margin-top:15px}
.blog-body .btn{background:#000;width:131px;height:49px;line-height:49px;text-align:center;font-size:15px;margin-top:31px}

/* footer */
.site-footer{height:186px}
.site-footer .wrap{display:flex;justify-content:space-between;padding-top:48px}
.site-footer .brand{margin-top:0}
.footer-right{text-align:right}
.footer-nav{display:flex;gap:50px;justify-content:flex-end}
.footer-nav a{font-size:17px;color:#222;text-decoration:none}
.copyright{font-size:14px;color:#222;margin-top:40px}
</style>
</head>
<body>

<div class="info-bar">
  <div class="wrap">
    <span><svg viewBox="0 0 24 24"><path d="M12 2a7 7 0 0 0-7 7c0 5 7 13 7 13s7-8 7-13a7 7 0 0 0-7-7zm0 9.5A2.5 2.5 0 1 1 12 6.5a2.5 2.5 0 0 1 0 5z"/></svg>#154 Lorem Ipsum Dummy Text Lorem Ipsum</span>
    <span><svg viewBox="0 0 24 24"><path d="M12 2a10 10 0 1 0 0 20 10 10 0 0 0 0-20zm0 18a8 8 0 1 1 0-16 8 8 0 0 1 0 16zm1-13h-2v6l5 3 1-1.6-4-2.4z"/></svg>Opening Time : Mon-Sat : 09:00am to10:00pm / Sunday Closed</span>
  </div>
</div>

<header class="site-header">
  <div class="wrap">
    <div class="brand">Amber Quill<small>Floristen &amp; Gärtner</small></div>
    <nav class="quick-nav">
      <a href="#"><svg viewBox="0 0 24 24"><path d="M6.6 10.8a15 15 0 0 0 6.6 6.6l2.2-2.2c.3-.3.7-.4 1-.2 1.1.4 2.3.6 3.6.6.6 0 1 .4 1 1V20c0 .6-.4 1-1 1A17 17 0 0 1 3 4c0-.6.4-1 1-1h3.5c.6 0 1 .4 1 1 0 1.3.2 2.5.6 3.6.1.3 0 .7-.2 1z"/></svg>Call</a>
      <a href="#"><svg viewBox="0 0 24 24"><path d="M2 5h20v3l-10 6L2 8zm0 5 10 6 10-6v9H2z"/></svg>Mail</a>
      <a href="#"><svg viewBox="0 0 24 24"><path d="M12 2a10 10 0 1 0 0 20 10 10 0 0 0 0-20zm-1 17.9A8 8 0 0 1 4.2 10l4.8 4.8v1a2 2 0 0 0 2 2zm6.9-2.5A2 2 0 0 0 16 16h-1v-3a1 1 0 0 0-1-1H8v-2h2a1 1 0 0 0 1-1V7h2a2 2 0 0 0 2-2v-.4a8 8 0 0 1 2.9 12.8z"/></svg>Web</a>
      <a href="#"><svg viewBox="0 0 24 24"><path d="M3 5l6-2 6 2 6-2v16l-6 2-6-2-6 2zm6 0v14m6-12v14" stroke="#fff" stroke-width="1.5"/></svg>Route</a>
      <a href="#"><svg viewBox="0 0 24 24"><ellipse cx="12" cy="5" rx="8" ry="3"/><path d="M4 7c0 1.7 3.6 3 8 3s8-1.3 8-3v4c0 1.7-3.6 3-8 3s-8-1.3-8-3zm0 6c0 1.7 3.6 3 8 3s8-1.3 8-3v4c0 1.7-3.6 3-8 3s-8-1.3-8-3z"/></svg>Data</a>
    </nav>
  </div>
</header>

<section class="hero" role="img" aria-label="Photo of hands typing on a laptop with a search bar overlay">
  <h1 class="hero-title">Amber Quill</h1>
  <p class="hero-sub">Search Engine For the Amber Quill - Business</p>
  <div class="thumbs">
    <div class="thumb t1 active" role="img" aria-label="Thumbnail: laptop with search bar"></div>
    <div class="thumb t2" role="img" aria-label="Thumbnail: hand with pen over a stock chart"></div>
    <div class="thumb t3" role="img" aria-label="Thumbnail: people reviewing printed charts"></div>
  </div>
</section>

<section class="about">
  <div class="wrap">
    <h2 class="heading">About <em>Us</em></h2>
    <p class="about-text">Sed ut perspiciatis unde omnis iste natus error sit voluptatem acc usantium doloremque laudantium, totam rem aperiam, eaque ipsa quae ab illo inventore veritatis et quasi architecto beatae vitae dicta sunt explicabo. Nemo enim ipsam volu ptatem quia voluptas sit aspernatur aut odit aut fugit, sed quia consequuntur magni dolores eos qui ratione voluptatem sequi nesciunt.Neque porro quisquam est, qui dolorem ipsum quia dolor sit amet, consectetur, adipisci dolore magnam aliquam quaerat voluptatem.</p>
    <a class="btn" href="#">Read More</a>
    <div class="about-slider" role="img" aria-label="Slider photo of a woman with glasses looking at a screen with a Searching overlay">
      <div class="dots"><i></i><i></i><i></i></div>
    </div>
  </div>
</section>

<section class="products">
  <div class="wrap">
    <h2 class="heading heading-center">Our <em>Products</em></h2>
    <div class="rule"></div>
    <div class="cards">
      <article class="product">
        <div class="pic p1" role="img" aria-label="Address book illustration"></div>
        <div class="price">$25.99</div>
        <h3 class="pname">Product Name</h3>
        <p class="pdesc">Sed ut perspiciatis unde omnis iste natus error sit voluptatem accusantium</p>
      </article>
      <article class="product">
        <div class="pic p2" role="img" aria-label="Map with location pin illustration"></div>
        <div class="price">$25.99</div>
        <h3 class="pname">Product Name</h3>
        <p class="pdesc">Sed ut perspiciatis unde omnis iste natus error sit voluptatem accusantium</p>
      </article>
      <article class="product">
        <div class="pic p3" role="img" aria-label="Red rotary telephone illustration"></div>
        <div class="price">$25.99</div>
        <h3 class="pname">Product Name</h3>
        <p class="pdesc">Sed ut perspiciatis unde omnis iste natus error sit voluptatem accusantium</p>
      </article>
    </div>
  </div>
</section>

<section class="services">
  <div class="wrap">
    <h2 class="heading heading-center">Our <em>Services</em></h2>
    <div class="rule"></div>
    <div class="service-row">
      <article class="service"><div class="pic s1" role="img" aria-label="Map with coloured push pins"></div><p>Sed ut perspiciatis<br>unde omnis</p></article>
      <article class="service"><div class="pic s2" role="img" aria-label="Hand with stylus over a financial chart"></div><p>Sed ut perspiciatis<br>unde omnis</p></article>
      <article class="service"><div class="pic s3" role="img" aria-label="Tablet showing analytics charts"></div><p>Sed ut perspiciatis<br>unde omnis</p></article>
      <article class="service"><div class="pic s4" role="img" aria-label="Pen resting on a printed chart"></div><p>Sed ut perspiciatis<br>unde omnis</p></article>
    </div>
  </div>
</section>

<section class="blog">
  <div class="blog-pic" role="img" aria-label="Desk with notebook sketch about SEO, plant and coffee cup"></div>
  <div class="blog-body">
    <h2 class="heading">Latest Blog</h2>
    <div class="rule"></div>
    <p class="blog-meta">08 August 2020 / Comments (05)</p>
    <p class="blog-text">Sed ut perspiciatis unde omnis iste natus error sit voluptatem acc usantium doloremque laudantium, totam rem aperiam, eaque ip sa quae ab illo inventore veritatis et quasi architecto beatae vitae dicta sunt explicabo. Nemo enim ipsam voluptatem quia voluptas sit aspernatur aut odit aut fugit, sed quia consequuntur magni dolores eos qui ratione voluptatem sequi nesciunt. Neque porro quisquam est, qui dolorem ipsum quia dolor sit amet, consectetur</p>
    <a class="btn" href="#">Read More</a>
  </div>
</section>

<footer class="site-footer">
  <div class="wrap">
    <div class="brand">Amber Quill<small>Floristen &amp; Gärtner</small></div>
    <div class="footer-right">
      <nav class="footer-nav"><a href="#">Call</a><a href="#">Mail</a><a href="#">Web</a><a href="#">Route</a><a href="#">Data</a></nav>
      <p class="copyright">© Copyright 2020 Amber Quill.All Rights Reserved</p>
    </div>
  </div>
</footer>

</body>
</html>
```